Used Car Dealer seeks an Amazing Business Card Design

We are looking for a business card design that incorporates our logo and grabs the attention of anyone we give the business card to.

Looking to use the same colors as the logo. Our Logo choice is the black background with Red and Silver/Grey Lettering.

We also would like to see some embossed designs.

Target Market(s)

Used Car Buyers, Automotive, Auto

Industry/Entity Type

Automotive

Contact Information for Business Card

BVEL7K
Gordon Whitlock
482 Tarrow Lane
Suite 207
Brenford, GA 30412
Office (770) 555-0142
Cell (770) 555-0187
bvel7kga@quellmail.com
www.bvel7kga.com

Colors
ffffff
ee3036

Requirements
Must have
• Must include our logo (Black Background with Red and Silver/Grey Lettering)
Nice to have
• Embossed Design. Can be Single or Double Sided.

```html
<!DOCTYPE html>
<html lang="en">
<head>
<meta charset="utf-8">
<title>BVEL7K Business Card</title>
<link href="https://fonts.googleapis.com/css2?family=Lato:wght@400;700;900&display=swap" rel="stylesheet">
<style>
  :root {
    --page: #e9e6e1;
    --card: #050505;
    --red: #ee3036;
    --white: #ffffff;
    --silver-light: #f2f2f2;
    --silver-dark: #9a9a9a;
  }
  * { margin: 0; padding: 0; box-sizing: border-box; }
  html, body { width: 1200px; height: 900px; overflow: hidden; }
  body {
    background: var(--page);
    font-family: "Lato", sans-serif;
    position: relative;
  }
  .card {
    position: absolute;
    left: 250px;
    width: 700px;
    height: 400px;
    background: var(--card);
    overflow: hidden;
    box-shadow: 0 10px 24px rgba(0,0,0,0.35);
  }
  .card--back { top: 40px; }
  .card--front { top: 460px; }

  .brand-name {
    font-family: "Lato", sans-serif;
    font-weight: 900;
    color: var(--red);
    letter-spacing: 2px;
    line-height: 1;
  }
  .card--back .brand-name {
    position: absolute;
    left: 0; right: 0; top: 145px;
    text-align: center;
    font-size: 78px;
  }
  .card--back .web {
    position: absolute;
    left: 0; right: 0; top: 290px;
    text-align: center;
    color: var(--white);
    font-size: 20px;
  }
  .web .web-domain { color: var(--red); }

  .card--front .brand-name {
    position: absolute;
    left: 55px; top: 105px;
    font-size: 58px;
  }
  .divider {
    position: absolute;
    left: 345px; top: 120px;
    width: 3px; height: 210px;
    background: linear-gradient(to bottom, var(--red) 0 28%, var(--white) 28% 100%);
  }
  .details {
    position: absolute;
    left: 370px; top: 118px;
    color: var(--white);
  }
  .person-name { color: var(--red); font-weight: 900; font-size: 27px; line-height: 1.1; }
  .person-role { font-size: 22px; margin-bottom: 14px; }
  .address { font-size: 19px; line-height: 1.25; margin-bottom: 8px; }
  .contact-row { display: flex; align-items: center; gap: 8px; font-size: 19px; line-height: 1.45; }
  .contact-row svg { width: 18px; height: 18px; flex: none; }

  .bands { position: absolute; left: 0; bottom: 0; width: 700px; height: 50px; }
  .card--front .web {
    position: absolute;
    right: 40px; bottom: 9px;
    color: var(--white);
    font-size: 22px;
    font-weight: 700;
  }
</style>
</head>
<body>
  <section class="card card--back">
    <div class="brand-name">BVEL7K</div>
    <p class="web">www.<span class="web-domain">bvel7kga</span>.com</p>
  </section>

  <section class="card card--front">
    <div class="brand-name">BVEL7K</div>
    <div class="divider"></div>
    <div class="details">
      <p class="person-name">Gordon Whitlock</p>
      <p class="person-role">Owner</p>
      <p class="address">482 Tarrow Lane<br>Suite 207 Brenford, GA 30412</p>
      <p class="contact-row">
        <svg viewBox="0 0 18 18" aria-hidden="true"><rect width="18" height="18" rx="3" fill="var(--red)"/><path d="M5 4c1-1 2 0 2.5 1.5S7 7 7 7.5 9.5 11 10.5 11s1-1 2-0.5 2 1.5 1 2.5c-2 2-9-4-8.5-9z" fill="var(--white)"/></svg>
        (770) 555-0142
      </p>
      <p class="contact-row">
        <svg viewBox="0 0 18 18" aria-hidden="true"><rect width="18" height="18" rx="3" fill="var(--red)"/><rect x="6" y="3" width="6" height="12" rx="1" fill="none" stroke="var(--white)" stroke-width="1.5"/></svg>
        (770) 555-0187
      </p>
      <p class="contact-row">
        <svg viewBox="0 0 18 18" aria-hidden="true"><rect width="18" height="18" rx="3" fill="var(--red)"/><rect x="3" y="5" width="12" height="8" fill="none" stroke="var(--white)" stroke-width="1.4"/><path d="M3 5l6 5 6-5" fill="none" stroke="var(--white)" stroke-width="1.4"/></svg>
        bvel7kga@quellmail.com
      </p>
    </div>
    <svg class="bands" viewBox="0 0 700 50" aria-hidden="true">
      <defs>
        <linearGradient id="silverBand" x1="0" y1="0" x2="0" y2="1">
          <stop offset="0" stop-color="var(--silver-light)"/>
          <stop offset="1" stop-color="var(--silver-dark)"/>
        </linearGradient>
      </defs>
      <polygon points="0,14 320,14 300,50 0,50" fill="url(#silverBand)"/>
      <polygon points="320,4 700,4 700,50 296,50" fill="var(--red)"/>
    </svg>
    <p class="web">www.bvel7kga.com</p>
  </section>
</body>
</html>
```